Упаковка снеков из морской капусты
Задание на дизайн
Приоритеты объектов в упаковке
Знак производителя, Марка продукта, Вид продукта, Название продукта, Иллюстрация
Опишите свою организацию или продукт и целевую аудиторию
сушеная морская капуста спрессованная в тончайшие пропускающие свет листы,
она настолько высушена, что хрустит ломаясь и буквально тает во рту впитывая влагу. это очень вкусно, хочется есть еще и еще...во вторых это очень полезный продукт, это здоровье ,энергия, для тех кого любит удача и у которых большие планы кто знает что хочет от жизни.
Приложите логотипы или другие материалы
это обычная очень типичная упаковка
может сделать гоизонт общий преходящий на правую и левую стороны там с одной стороны красивая фигура мужчины с другой женщины
так выглядит сам продукт 10 тончайших пластинок спрессованной сушеной капусты
здесь красивый шрифт ,сам продукт и выдержана цветовая гамма
ИНФОРМАЦИОННЫЕ ЗНАЧКИ
Вот так выглядит сам продукт
здесь есть типа талисман
ЛОГОТИПЫ
Комментарии и пожелания для дизайнеров
хотелось бы увидеть оригинальные решения, обыграть саму упаковку (использовать боковые стороны),использовать например черно-белое фото и яркие цветные акценты...показать энергию, молодость, здоровье, успех...идея или две упаковки: для желающих вести здоровый образ мужчин и для довольных своей фигурой и счастливых женщин...или создать в одной упаковке и для мужчин и женщин. можно совсем немного добавить Азии например иероглиф ...возможны два вкуса васаби и оливок. Можно сделать две упаковки так, чтобы рисунок на одной был продолжением на другой и когда они стоят вместе на полке смотрятся как единое целое...может какие то другие идеи...

```html
<!DOCTYPE html>
<html lang="ru">
<head>
<meta charset="utf-8">
<title>Снеки из морской капусты — упаковка</title>
<link rel="stylesheet" href="https://fonts.googleapis.com/css2?family=Amatic+SC:wght@400;700&family=Ruslan+Display&family=Roboto:wght@400;700&display=swap">
<style>
  :root {
    --pack-green: #087a0a;
    --accent-cyan: #12c3e6;
    --accent-yellow: #f7c514;
    --accent-magenta: #c01a8e;
    --accent-pink: #ee1e72;
    --slogan-lime: #c9e24a;
    --ink-dark: #1b1b1b;
    --text-white: #ffffff;
    --brand-teal: #2aa6b4;
  }
  html, body {
    margin: 0;
    padding: 0;
    width: 1200px;
    height: 800px;
    overflow: hidden;
    background: #ffffff;
  }
  .canvas {
    position: relative;
    width: 1200px;
    height: 800px;
    overflow: hidden;
    background: #ffffff;
  }
  .pack {
    position: absolute;
    left: 24px;
    top: 11px;
    width: 1155px;
    height: 778px;
    background: var(--pack-green);
    overflow: hidden;
  }
  .top-bands {
    position: absolute;
    left: 0;
    top: 0;
    width: 1155px;
    height: 90px;
  }
  .ornament {
    position: absolute;
    border-radius: 6px;
    opacity: 0.85;
  }
  .ornament-magenta { background: linear-gradient(180deg, var(--accent-magenta), #9a1572); }
  .ornament-pink { background: linear-gradient(180deg, var(--accent-pink), #c4185e); }
  .ornament-yellow { background: linear-gradient(180deg, var(--accent-yellow), #dba90e); }
  .ornament-cyan { background: linear-gradient(180deg, var(--accent-cyan), #0ea5c4); }

  .title {
    position: absolute;
    left: 0;
    width: 100%;
    text-align: center;
    top: 214px;
    margin: 0;
    font-family: "Ruslan Display", serif;
    font-weight: 400;
    font-size: 70px;
    line-height: 1;
    color: var(--ink-dark);
    -webkit-text-stroke: 8px var(--accent-yellow);
    paint-order: stroke fill;
    letter-spacing: 2px;
  }
  .subtitle {
    position: absolute;
    left: 0;
    width: 100%;
    top: 318px;
    text-align: center;
    font-family: "Ruslan Display", serif;
    font-size: 21px;
    line-height: 1;
    color: var(--text-white);
  }
  .flavour-label {
    position: absolute;
    left: 0;
    width: 100%;
    top: 354px;
    text-align: center;
    font-family: "Roboto", sans-serif;
    font-size: 16px;
    letter-spacing: 4px;
    color: var(--text-white);
  }
  .flavour-arrows {
    position: absolute;
    left: 0;
    top: 0;
    width: 1155px;
    height: 778px;
    pointer-events: none;
  }
  .flavour-ribbon {
    position: absolute;
    left: 488px;
    top: 377px;
    width: 190px;
    height: 34px;
  }
  .flavour-name {
    position: absolute;
    left: 488px;
    top: 385px;
    width: 190px;
    text-align: center;
    font-family: "Roboto", sans-serif;
    font-weight: 700;
    font-size: 15px;
    line-height: 18px;
    letter-spacing: 4px;
    color: var(--text-white);
  }
  .slogan {
    position: absolute;
    left: 0;
    width: 100%;
    top: 450px;
    margin: 0;
    text-align: center;
    font-family: "Amatic SC", sans-serif;
    font-weight: 400;
    font-size: 50px;
    line-height: 58px;
    color: var(--slogan-lime);
  }
  .brand {
    position: absolute;
    left: 0;
    width: 100%;
    top: 668px;
    display: flex;
    justify-content: center;
    align-items: center;
    gap: 12px;
  }
  .brand-mark {
    width: 26px;
    height: 26px;
    background: var(--brand-teal);
  }
  .brand-name {
    font-family: "Roboto", sans-serif;
    font-weight: 700;
    font-size: 40px;
    letter-spacing: 3px;
    color: var(--brand-teal);
  }
  .info {
    position: absolute;
    top: 292px;
    font-family: "Roboto", sans-serif;
    font-size: 9.5px;
    line-height: 12px;
  }
  .info p { margin: 0 0 12px; }
  .info-left {
    left: 52px;
    width: 160px;
    color: var(--text-white);
  }
  .info-right {
    left: 960px;
    width: 170px;
    color: var(--slogan-lime);
  }
  .nutrient-row {
    display: flex;
    justify-content: space-between;
  }
  .macros {
    position: absolute;
    top: 730px;
    left: 200px;
    display: flex;
    gap: 8px;
    font-family: "Roboto", sans-serif;
    font-size: 11px;
    line-height: 14px;
    color: var(--ink-dark);
  }
  .macro { padding: 0 6px; }
  .macro-carbs { background: var(--accent-pink); }
  .macro-fat { background: var(--accent-yellow); }
  .macro-protein { background: var(--accent-cyan); }
</style>
</head>
<body>
<div class="canvas">
  <div class="pack">
    <svg class="top-bands" viewBox="0 0 1155 90" aria-hidden="true">
      <g fill="none" stroke="var(--accent-cyan)" stroke-width="6">
        <line x1="0" y1="22" x2="1155" y2="14"/>
        <line x1="0" y1="42" x2="1155" y2="34"/>
        <line x1="0" y1="62" x2="1155" y2="54"/>
      </g>
    </svg>

    <div class="ornament ornament-magenta" role="img" aria-label="Декоративная вертикальная волна" style="left:96px; top:82px; width:16px; height:195px;"></div>
    <div class="ornament ornament-yellow" role="img" aria-label="Декоративный элемент" style="left:290px; top:147px; width:52px; height:52px;"></div>
    <div class="ornament ornament-yellow" role="img" aria-label="Декоративный элемент" style="left:1038px; top:114px; width:62px; height:52px;"></div>
    <div class="ornament ornament-cyan" role="img" aria-label="Декоративный элемент" style="left:792px; top:198px; width:64px; height:64px;"></div>
    <div class="ornament ornament-pink" role="img" aria-label="Декоративные волнистые линии" style="left:284px; top:516px; width:156px; height:74px;"></div>
    <div class="ornament ornament-yellow" role="img" aria-label="Декоративные зигзаги" style="left:752px; top:566px; width:106px; height:60px;"></div>
    <div class="ornament ornament-yellow" role="img" aria-label="Декоративный элемент" style="left:195px; top:585px; width:64px; height:64px;"></div>
    <div class="ornament ornament-magenta" role="img" aria-label="Декоративный элемент" style="left:832px; top:692px; width:60px; height:60px; border-radius:50%;"></div>
    <div class="ornament ornament-pink" role="img" aria-label="Декоративный элемент" style="left:0; top:628px; width:16px; height:34px;"></div>
    <div class="ornament ornament-cyan" role="img" aria-label="Декоративные линии" style="left:20px; top:722px; width:84px; height:56px;"></div>

    <h1 class="title">СНЕКИ</h1>
    <div class="subtitle">из морской капусты</div>
    <svg class="flavour-arrows" viewBox="0 0 1155 778" aria-hidden="true">
      <g stroke="var(--accent-yellow)" stroke-width="2" fill="var(--accent-yellow)">
        <line x1="512" y1="362" x2="546" y2="362"/>
        <polygon points="508,362 515,358 515,366"/>
        <line x1="610" y1="362" x2="644" y2="362"/>
        <polygon points="648,362 641,358 641,366"/>
      </g>
    </svg>
    <div class="flavour-label">вкус</div>
    <svg class="flavour-ribbon" viewBox="0 0 190 34" aria-hidden="true">
      <path d="M0 6 L190 6 L180 17 L190 28 L0 28 L10 17 Z" fill="var(--accent-yellow)"/>
    </svg>
    <div class="flavour-name">оливки</div>

    <p class="slogan">Суперполезно<br>ну очень вкусно<br>хрум-хрум</p>

    <div class="brand">
      <span class="brand-mark"></span>
      <span class="brand-name">SEALEAF</span>
    </div>

    <div class="info info-left">
      <p>Наименование продукта:<br>Сушеная морская капуста</p>
      <p>Масса нетто: 4,5г<br>Состав: сушеная морская капуста 88%, рапсовое масло 9%, периллевое масло 1%, кунжутное масло 1%, соль 1%</p>
      <p style="margin-top:24px">Производитель:<br>CHIOKAN CO.<br>8, Хэан-ро, Сокчхо-си, Канвон-до, Республика Корея</p>
      <p>Импортер: ООО «Velmora»<br>Россия, Камчатский Край г.Елизово ул. Приморская 7-3<br>тел: +7 900 000-00-00<br>www.velmora-food.ru</p>
    </div>

    <div class="info info-right">
      <p>Пищевая энергетическая ценность (на 100г.)<br>Калорийность - 2142 кДж/510 ккал</p>
      <div class="nutrient-row"><span>Углеводы</span><span>33.5 г</span></div>
      <div class="nutrient-row"><span>Белки</span><span>23г</span></div>
      <div class="nutrient-row"><span>Жиры</span><span>30.5г</span></div>
      <div class="nutrient-row"><span>Натрий</span><span>1987.5 мг</span></div>
      <p>Условия хранения: хранить в прохладном месте, защищенном от света и влаги месте, при температуре от -5С до + 25 С</p>
    </div>

    <div class="macros">
      <span class="macro macro-carbs">У 33,5 г</span>
      <span class="macro macro-fat">Ж30,5 г</span>
      <span class="macro macro-protein">Б23г</span>
    </div>
  </div>
</div>
</body>
</html>
```